ambitious event and festival agency from austria needs fresh business card design

A new design is due for the new headquarters and the new challenges. We organize events for different target groups from 16 to 60 years. The design should therefore be straightforward and not confused, so we are open to new colors and the logo may also be changed. In general, however, the most interesting suggestions are the most interesting ones. after this order we are looking for more graphics for partyvelt facebook instagramm homepage etc A new design is due for the new headquarters and the new challenges. We organize events for different target groups from 16 to 60 years. The design should therefore be straightforward and not confused, so we are open to new colors and the logo may also be changed. In general, however, the most interesting suggestions are the most interesting ones. after this order we are looking for more graphics for partyvelt facebook instagramm homepage etc A new design is due for the new headquarters and the new challenges. We organize events for different target groups from 16 to 60 years. The design should therefore be straightforward and not confused, so we are open to new colors and the logo may also be changed. In general, however, the most interesting suggestions are the most interesting ones. after this order we are looking for more graphics for partyvelt facebook instagramm homepage etc

Reason: I am sorry for this decision but i need some more time. No new designs please, there are so many good ones and I will have made a decision in the next 3 days.

Target Market(s)

Industry/Entity Type

Business

Font styles to use
Serif
Sans Serif

Colors

Designer to choose colors to be used in the design.

Requirements
Must have
Nice to have
Should not have

```html
<!DOCTYPE html>
<html lang="en">
<head>
<meta charset="utf-8">
<title>partyvelt – Business Card</title>
<link href="https://fonts.googleapis.com/css2?family=Source+Sans+3:wght@400;600;700&display=swap" rel="stylesheet">
<style>
  :root {
    --backdrop: #000000;
    --card: #323235;
    --text-light: #f2f2f2;
    --text-soft: #e4e4e4;
    --brand-red: #b82a37;
    --divider: rgba(255, 255, 255, 0.08);
  }
  * { margin: 0; padding: 0; box-sizing: border-box; }
  html, body {
    width: 1200px;
    height: 900px;
    overflow: hidden;
    background: var(--backdrop);
    font-family: "Source Sans 3", "Helvetica Neue", Arial, sans-serif;
  }
  .canvas { position: relative; width: 1200px; height: 900px; }
  .card {
    position: absolute;
    top: 271px;
    width: 457px;
    height: 281px;
    border-radius: 14px;
    background: var(--card);
  }
  .card--front { left: 137px; }
  .card--back { left: 626px; }

  .brand-block {
    position: absolute;
    left: 40px;
    top: 0;
    width: 184px;
    height: 281px;
    display: flex;
    align-items: center;
    justify-content: center;
  }
  .brand-name {
    color: var(--brand-red);
    font-weight: 700;
    font-size: 32px;
    letter-spacing: -0.5px;
  }
  .divider {
    position: absolute;
    left: 224px;
    top: 80px;
    width: 1px;
    height: 140px;
    background: var(--divider);
  }
  .contact {
    position: absolute;
    left: 255px;
    top: 72px;
    color: var(--text-soft);
  }
  .contact__name {
    font-size: 19px;
    font-weight: 600;
    color: var(--text-light);
    line-height: 22px;
  }
  .contact__role { font-size: 13px; line-height: 16px; }
  .contact__address { margin-top: 11px; font-size: 13px; line-height: 16px; }
  .contact__list { list-style: none; margin-top: 11px; font-size: 13px; line-height: 16.5px; }
  .contact__list li { display: flex; align-items: center; gap: 7px; }
  .contact__list svg { width: 10px; height: 10px; fill: var(--text-soft); flex: none; }

  .card--back .brand-name {
    position: absolute;
    left: 0; right: 0;
    top: 115px;
    text-align: center;
    font-size: 50px;
    font-weight: 600;
    line-height: 50px;
  }
</style>
</head>
<body>
<main class="canvas">
  <section class="card card--front">
    <div class="brand-block"><span class="brand-name">partyvelt</span></div>
    <div class="divider"></div>
    <div class="contact">
      <p class="contact__name">Lukas Berger</p>
      <p class="contact__role">Managing Director</p>
      <p class="contact__address">Lindengasse 14, Top 5<br>Austria, 1070 Wien.</p>
      <ul class="contact__list">
        <li><svg viewBox="0 0 10 10" aria-hidden="true"><path d="M2 0.5l1.6 2-1 1.2c.6 1.3 1.5 2.2 2.7 2.8l1.2-1 2 1.6-.8 1.9C4.6 9 1 5.4 0.1 1.3z"/></svg>043-660 218 547</li>
        <li><svg viewBox="0 0 10 10" aria-hidden="true"><path d="M0.5 2h9v6h-9z M1 2.5l4 3 4-3" stroke="#323235" stroke-width="0.8"/></svg>hello@partyvelt.at</li>
        <li><svg viewBox="0 0 10 10" aria-hidden="true"><path d="M4 6l2-2M3.2 4.6l-1.4 1.4a1.6 1.6 0 002.2 2.2l1.4-1.4M6.8 5.4l1.4-1.4a1.6 1.6 0 00-2.2-2.2L4.6 3.2" fill="none" stroke="#e4e4e4" stroke-width="1.1" stroke-linecap="round"/></svg>www.partyvelt.at</li>
      </ul>
    </div>
  </section>

  <section class="card card--back">
    <span class="brand-name">partyvelt</span>
  </section>
</main>
</body>
</html>
```